Business Card Design Project

KB Consulting Associates is a management consulting business with C-suite (CEO/CFO etc) target clients. Logo selected is blue with simple/serious typefaces.

Target Market(s)

CEOs and CFOs of large corporates

Industry/Entity Type

Management Consulting

Font styles to use
Serif

Colors
3276b5

Requirements
Must have
• Tag line: Building successful collaborations (use different font)
Address: 427 Fernvale Crescent #03-22 Singapore 519337
Telephone: +65 8372 4096
Email: kbloh@postnest42.com

```html
<!DOCTYPE html>
<html lang="en">
<head>
<meta charset="utf-8">
<title>KB Consulting Associates – Business Card</title>
<link rel="stylesheet" href="https://fonts.googleapis.com/css2?family=Libre+Baskerville:wght@400&family=Open+Sans:ital,wght@0,400;1,400&display=swap">
<style>
  :root {
    --page: #e9e7e3;
    --slate: #4c5d6b;
    --slate-light: #5a6b79;
    --navy: #1f3547;
    --navy-band: #24394b;
    --brand-blue: #3276b5;
    --ink-light: #ffffff;
    --ink-soft: #c9d7e4;
  }
  * { box-sizing: border-box; margin: 0; padding: 0; }
  html, body { width: 1200px; height: 1000px; overflow: hidden; background: var(--page); }
  .sheet {
    width: 1200px; height: 1000px;
    display: flex; align-items: center; justify-content: center; gap: 60px;
  }
  .card {
    position: relative; width: 540px; height: 310px; overflow: hidden;
    box-shadow: 0 6px 18px rgba(0,0,0,.18);
    font-family: "Libre Baskerville", serif; color: var(--ink-light);
  }
  .card__bg { position: absolute; inset: 0; width: 100%; height: 100%; }
  .brand { position: absolute; left: 0; right: 0; text-align: center; }
  .brand__mark {
    display: block; width: 38px; height: 38px; margin: 0 auto 12px;
    background: var(--brand-blue);
  }
  .brand__name {
    font-weight: 400; font-size: 24px; letter-spacing: .5px; text-transform: uppercase; line-height: 1;
    white-space: nowrap;
  }
  .brand__tagline {
    font-family: "Open Sans", sans-serif; font-style: italic; font-size: 12px; letter-spacing: .6px;
    color: var(--ink-soft); margin-top: 8px; padding-left: 90px;
  }
  .card--front .brand { top: 100px; padding-left: 30px; }

  .card--back .brand { top: 30px; padding-left: 30px; }
  .card--back .brand__name { font-size: 21px; }
  .card--back .brand__mark { width: 32px; height: 32px; }
  .card--back .brand__tagline { font-size: 11px; }
  .contacts {
    position: absolute; left: 0; right: 0; top: 196px; height: 114px;
    display: flex; justify-content: space-between; padding: 22px 22px 0;
    font-family: "Open Sans", sans-serif; font-size: 11px; line-height: 1.7;
  }
  .contact-group { list-style: none; }
  .contact-group li { display: flex; align-items: center; gap: 8px; white-space: nowrap; }
  .contact-group svg { width: 11px; height: 11px; flex: none; fill: var(--ink-light); }
  .contact-group .indent { padding-left: 19px; }
</style>
</head>
<body>
<main class="sheet">

  <section class="card card--front" aria-label="Business card front">
    <svg class="card__bg" viewBox="0 0 540 310" preserveAspectRatio="none" aria-hidden="true">
      <rect width="540" height="310" fill="var(--slate)"/>
      <polygon fill="var(--navy)" points="232,0 540,0 540,310 212,310 216,290 208,270 214,248 206,226 212,204 204,182 210,160 202,138 210,116 204,94 214,72 208,50 220,28 214,12"/>
    </svg>
    <div class="brand">
      <span class="brand__mark"></span>
      <p class="brand__name">KB Consulting Associates</p>
      <p class="brand__tagline">Building successful collaborations</p>
    </div>
  </section>

  <section class="card card--back" aria-label="Business card back">
    <svg class="card__bg" viewBox="0 0 540 310" preserveAspectRatio="none" aria-hidden="true">
      <rect width="540" height="310" fill="var(--slate-light)"/>
      <rect y="196" width="540" height="114" fill="var(--slate)"/>
      <polygon fill="var(--navy)" points="300,0 540,0 540,310 280,310 286,286 276,262 284,238 274,214 282,190 272,166 280,142 270,118 278,94 270,70 282,46 276,22"/>
      <rect x="280" y="196" width="260" height="114" fill="var(--navy-band)"/>
      <rect y="194" width="540" height="2" fill="var(--brand-blue)"/>
    </svg>
    <div class="brand">
      <span class="brand__mark"></span>
      <p class="brand__name">KB Consulting Associates</p>
      <p class="brand__tagline">Building successful collaborations</p>
    </div>
    <div class="contacts">
      <ul class="contact-group contact-group--address">
        <li><svg viewBox="0 0 12 12"><path d="M6 0a4 4 0 0 0-4 4c0 3 4 8 4 8s4-5 4-8a4 4 0 0 0-4-4zm0 5.6A1.6 1.6 0 1 1 6 2.4a1.6 1.6 0 0 1 0 3.2z"/></svg>427 Fernvale Crescent #03-22</li>
        <li class="indent">Singapore 519337</li>
      </ul>
      <ul class="contact-group contact-group--phone">
        <li><svg viewBox="0 0 12 12"><path d="M2.5 0.5l2 2.6-1.2 1.4c.8 1.7 2.2 3.1 3.9 3.9l1.4-1.2 2.6 2-1.3 2.3C5 11 1 7 .3 1.8z"/></svg>+65 8372 4096</li>
      </ul>
      <ul class="contact-group contact-group--web">
        <li><svg viewBox="0 0 12 12"><circle cx="6" cy="6" r="5.5"/></svg>www.kbconsulting-sg.net</li>
        <li><svg viewBox="0 0 12 12"><path d="M0 2h12v8H0zm1 1v.4l5 3.2 5-3.2V3z"/></svg>kbloh@postnest42.com</li>
      </ul>
    </div>
  </section>

</main>
</body>
</html>
```